Walking Beside the Quiet River; A Study of Refuge, Purpose & Calling

I need a book cover, for the above book title. This is a journey of the heart to know the heart of God. I think on the text, Simple (see below graphic)
Black Lettering for Knowing.....Intimately
Gold lettering for God
Either gold or black for the subtitle; A Study of Refuge, Purpose, & Calling
I would like the below graphic idea only no photograph of a person,
and White background instead of black
Simple Font, like below graphic, but open to suggestions

Target Market(s)

not age specific, Every person has been given a heart to know God, we are taking the mystery out the process to understand God is Father, loving gracious, ever present, etc. If we know His heart, we realize He's not at a distance, He is there, an ever present help

Industry/Entity Type

Security

Requirements
Must have
• Title: Walking Beside the Quiet River; A Study of Refuge, Purpose, & Calling
• My name, Tom Pettigrew
Nice to have
• See Below Graphic

```html
<!DOCTYPE html>
<html lang="en">
<head>
<meta charset="utf-8">
<title>Walking Beside the Quiet River — Tom Pettigrew</title>
<link rel="stylesheet" href="https://fonts.googleapis.com/css2?family=Jost:wght@400;500;600&display=swap">
<style>
  :root {
    --sky-top: #6f93b8;
    --sky-mid: #a9cad6;
    --mist: #d3e8e2;
    --haze: #e3e6c8;
    --ground: #a79d80;
    --ink: #0d0d0d;
    --author: #f1ddc0;
    --gold-light: #f4e7a6;
    --gold-mid: #c9a84a;
    --gold-deep: #6e5418;
  }
  html, body {
    margin: 0;
    padding: 0;
    width: 801px;
    height: 1200px;
    overflow: hidden;
  }
  .cover {
    position: relative;
    width: 801px;
    height: 1200px;
    overflow: hidden;
    font-family: "Jost", "Futura", sans-serif;
    text-align: center;
  }
  .cover-backdrop {
    position: absolute;
    inset: 0;
    background:
      radial-gradient(ellipse 90% 40% at 20% 45%, rgba(225,242,236,0.9), rgba(225,242,236,0) 70%),
      radial-gradient(ellipse 70% 30% at 90% 95%, rgba(120,110,85,0.55), rgba(120,110,85,0) 70%),
      linear-gradient(200deg, var(--sky-top) 0%, var(--sky-mid) 28%, var(--mist) 52%, var(--haze) 72%, var(--ground) 100%);
  }
  .author {
    position: absolute;
    top: 118px;
    left: 0;
    right: 0;
    margin: 0;
    font-weight: 600;
    font-size: 44px;
    letter-spacing: 0.07em;
    color: var(--author);
    text-shadow: 1px 2px 4px rgba(40,40,40,0.45);
  }
  .title {
    margin: 0;
    font-weight: 600;
  }
  .title-line {
    position: absolute;
    left: 0;
    right: 0;
    display: block;
    color: var(--ink);
  }
  .title-lead {
    top: 350px;
    font-size: 52px;
    letter-spacing: 0.06em;
  }
  .title-feature {
    top: 480px;
    font-size: 210px;
    line-height: 1;
    letter-spacing: 0.03em;
    font-weight: 500;
    background: linear-gradient(180deg, var(--gold-light) 0%, var(--gold-mid) 40%, var(--gold-deep) 62%, var(--gold-mid) 80%, var(--gold-light) 100%);
    -webkit-background-clip: text;
    background-clip: text;
    color: transparent;
    filter: drop-shadow(2px 4px 3px rgba(50,40,10,0.5));
  }
  .title-end {
    top: 800px;
    font-size: 88px;
    letter-spacing: 0.06em;
  }
  .subtitle {
    position: absolute;
    top: 962px;
    left: 0;
    right: 0;
    margin: 0;
    font-weight: 400;
    font-size: 32px;
    line-height: 1.2;
    letter-spacing: 0.04em;
    color: var(--ink);
  }
</style>
</head>
<body>
  <main class="cover">
    <div class="cover-backdrop" role="img" aria-label="Soft misty sky fading from blue at the top to pale hazy gold near the bottom"></div>
    <p class="author">TOM PETTIGREW</p>
    <h1 class="title">
      <span class="title-line title-lead">WALKING BESIDE THE</span>
      <span class="title-line title-feature">QUIET</span>
      <span class="title-line title-end">RIVER</span>
    </h1>
    <p class="subtitle">A Study of Refuge,<br>Purpose &amp; Calling</p>
  </main>
</body>
</html>
```